Law Firm Website

We are a small California based law firm specializing in business, corporate and litigation matters. We need to have our website redesigned. We are looking for a new and fresh look for our site, keeping in mind that we are a law firm.
What we don't want:
**the traditional "gavel" and "scales of justice" look
**anything too crazy
What we do want:
**sophisticated yet modern and fresh corporate look and feel
**samples of websites we really like:
http://www.mtrhllp-example.com
http://www.orwenlatch-example.com/
we also like:
http://www.verdtolbain-example.com/
http://www.qh-example.com/
http://www.pembrost-example.com/
http://www.nvtr-example.com
http://www.rmqlaw-example.com/
The content will be whatever is currently on our website (www.halvencourtlaw-example.com). We will be selecting the winner based on originality and keeping the above requirements in mind. Please note that the photos that you use will be the ones that we will be using, so choose wisely because the photos will make a difference.
Target Market(s)
Corporate clients
Industry/Entity Type
Law Firm
Look and feel

```html
<!DOCTYPE html>
<html lang="en">
<head>
<meta charset="utf-8">
<title>Halvencourt Law Group, LLP – Attorneys at Law</title>
<link href="https://fonts.googleapis.com/css2?family=Open+Sans:wght@400;600&family=Roboto+Condensed:wght@400&family=Arimo:wght@400;700&display=swap" rel="stylesheet">
<style>
:root{
  --blue:#2f6eae;
  --blue-dark:#24558a;
  --blue-light:#5b9be0;
  --tile-top:#3c78b3;
  --tile-bot:#245a90;
  --ink:#1d1d1d;
  --text:#3a3a3a;
  --muted:#555;
  --page:#f1f1f1;
  --band:#ebebeb;
  --rule:#c9c9c9;
  --foot-top:#4a4a4a;
  --foot-bot:#121212;
}
*{margin:0;padding:0;box-sizing:border-box}
html,body{width:978px;height:1200px;overflow:hidden}
body{position:relative;background:var(--page);font-family:"Open Sans",sans-serif;color:var(--text)}
.abs{position:absolute}

.masthead{left:0;top:0;width:978px;height:141px;background:linear-gradient(#fafafa,#e6e6e6)}
.brand-mark{left:85px;top:20px;width:53px;height:53px;background:var(--blue)}
.brand-name{left:145px;top:20px;font-size:21px;color:var(--ink);white-space:nowrap}
.brand-tag{left:173px;top:50px;font-size:16px;color:var(--ink)}
.phone{left:630px;top:33px;display:flex;align-items:center;gap:10px;font-size:16px;color:var(--blue)}
.social-top{left:762px;top:30px;display:flex;gap:7px}
.social-top span{width:28px;height:28px;border-radius:50%;background:#3a3a3a;display:block}

.nav{left:85px;top:94px;width:810px;height:47px;background:linear-gradient(var(--blue-light),var(--blue-dark));display:flex}
.nav a{color:#fff;text-decoration:none;font-size:14px;display:flex;align-items:center;justify-content:center;border-right:1px solid rgba(255,255,255,.35)}
.nav .home{width:47px;background:rgba(255,255,255,.12)}

.hero{left:85px;top:141px;width:810px;height:346px;background:linear-gradient(100deg,#f2f2f2 0%,#e2e2e2 45%,#8c8c8c 60%,#cfcfcf 80%,#6d6d6d 100%)}
.hero-arrow{top:292px;width:25px;height:41px;background:#2d2d2d;display:flex;align-items:center;justify-content:center}
.hero-caption{left:521px;top:374px;width:371px;height:85px;background:rgba(70,130,190,.55);color:#fff;font-size:29px;line-height:40px;text-align:center;padding-top:3px}
.hero-shadow{left:105px;top:487px;width:766px;height:33px;background:radial-gradient(ellipse at top,rgba(90,90,110,.45),rgba(0,0,0,0) 70%)}

.section-title{left:0;width:978px;top:526px;text-align:center;font-size:18px;color:var(--ink)}
.tile{top:563px;width:192px;height:107px;background:linear-gradient(var(--tile-top),var(--tile-bot));color:#fff;text-align:center}
.tile svg{margin-top:14px}
.tile p{position:absolute;left:0;right:0;top:75px;font-size:18px}

.band{left:0;top:707px;width:978px;height:364px;background:var(--band);border-top:1px solid var(--rule)}
.heading{font-family:"Roboto Condensed",sans-serif;font-size:21px;color:var(--ink);top:741px;letter-spacing:-.3px}
.team-photo{left:90px;top:775px;width:420px;height:166px;background:linear-gradient(90deg,#cfd3d8,#e8e3dc 40%,#d8dde3 70%,#c9b9b9)}
.about-copy{left:90px;top:950px;width:418px;font-family:Arimo,sans-serif;font-size:10.5px;line-height:16.3px;text-align:justify;color:var(--text)}
.more{left:434px;top:1018px;width:72px;height:22px;border-radius:11px;background:linear-gradient(#7a7a7a,#3e3e3e);color:#fff;font-family:Arimo,sans-serif;font-weight:700;font-size:11.5px;text-align:center;line-height:22px}
.news-nav{left:848px;top:739px;display:flex;gap:1px}
.news{left:535px;width:350px;height:80px}
.news .date{position:absolute;left:0;top:0;width:61px;height:69px;background:var(--blue-light);color:#fff;text-align:center}
.news .day{font-size:20px;line-height:40px;padding-top:3px}
.news .month{position:absolute;left:0;bottom:0;width:61px;height:22px;background:var(--blue);font-size:10px;line-height:22px}
.news h3{position:absolute;left:70px;top:0;font-family:"Roboto Condensed",sans-serif;font-weight:400;font-size:12px;color:var(--blue)}
.news h4{position:absolute;left:70px;top:15px;font-family:"Roboto Condensed",sans-serif;font-weight:400;font-size:12px;color:var(--ink)}
.news p{position:absolute;left:70px;top:35px;width:278px;font-family:Arimo,sans-serif;font-size:8.6px;line-height:11.8px;color:var(--muted);text-align:justify}
.news-rule{left:535px;width:350px;height:1px;background:var(--rule)}

.footer{left:0;top:1071px;width:978px;height:129px;background:linear-gradient(var(--foot-top),var(--foot-bot))}
.foot-links{left:0;width:978px;top:1091px;text-align:center;font-family:Arimo,sans-serif;font-size:10.5px;color:#fff}
.copyright{left:90px;top:1144px;font-family:Arimo,sans-serif;font-size:9.5px;color:#e6e6e6}
.social-foot{left:380px;top:1129px;display:flex;gap:6px}
.social-foot span{width:32px;height:32px;border-radius:50%;background:#f2f2f2;display:block}
.newsletter{left:699px;top:1135px;width:196px;height:23px;background:#fff;font-family:Arimo,sans-serif;font-style:italic;font-size:10px;color:#555;padding:6px 0 0 9px}
.newsletter svg{position:absolute;right:8px;top:4px}
</style>
</head>
<body>

<header>
  <div class="abs masthead"></div>
  <div class="abs brand-mark"></div>
  <div class="abs brand-name">Halvencourt Law Group, LLP</div>
  <div class="abs brand-tag">Attorneys at Law</div>
  <div class="abs phone">
    <svg width="12" height="20" viewBox="0 0 12 20"><rect x="1" y="1" width="10" height="18" rx="2" fill="none" stroke="#8a8a8a" stroke-width="1.6"/><rect x="3" y="4" width="6" height="10" fill="#8a8a8a"/></svg>
    <span>555.014.2290</span>
  </div>
  <div class="abs social-top"><span></span><span></span><span></span><span></span></div>

  <nav class="abs nav">
    <a class="home" href="#"><svg width="20" height="18" viewBox="0 0 20 18"><path d="M10 1 1 9h3v8h4v-5h4v5h4V9h3z" fill="#fff"/></svg></a>
    <a href="#" style="width:139px">ABOUT HLG</a>
    <a href="#" style="width:136px">PRACTICE AREAS</a>
    <a href="#" style="width:67px">LINKS</a>
    <a href="#" style="width:94px">CONTACT</a>
  </nav>
</header>

<section>
  <div class="abs hero" role="img" aria-label="Attorney in a light suit standing before the stone columns of a courthouse"></div>
  <div class="abs hero-arrow" style="left:85px"><svg width="10" height="14" viewBox="0 0 10 14"><path d="M8 1 2 7l6 6" fill="none" stroke="#fff" stroke-width="2.5"/></svg></div>
  <div class="abs hero-arrow" style="left:870px"><svg width="10" height="14" viewBox="0 0 10 14"><path d="M2 1l6 6-6 6" fill="none" stroke="#fff" stroke-width="2.5"/></svg></div>
  <div class="abs hero-caption">WE PROVIDE LEGAL<br>HELP FOR</div>
  <div class="abs hero-shadow"></div>
</section>

<section>
  <h2 class="abs section-title" style="font-weight:400">PRACTICE AREAS</h2>
  <div class="abs tile" style="left:84px">
    <svg width="56" height="48" viewBox="0 0 56 48"><path d="M20 4h34v32H20zM4 20l8-10h6v26H2V22z" fill="#fff"/><circle cx="12" cy="40" r="6" fill="#fff" stroke="#2f6eae" stroke-width="3"/><circle cx="44" cy="40" r="6" fill="#fff" stroke="#2f6eae" stroke-width="3"/></svg>
    <p>Auto Accidents</p>
  </div>
  <div class="abs tile" style="left:291px">
    <svg width="50" height="62" viewBox="0 0 50 62"><path d="M28 2c-14 12-12 24-8 34 3 7 12 6 14-2 2-8-4-14-6-32z" fill="#fff"/><rect x="2" y="54" width="46" height="4" fill="#fff"/></svg>
    <p>Burn Injuries</p>
  </div>
  <div class="abs tile" style="left:497px">
    <svg width="64" height="48" viewBox="0 0 64 48"><rect x="2" y="4" width="60" height="40" fill="#fff"/><rect x="10" y="11" width="44" height="26" fill="#2f6eae"/><circle cx="32" cy="24" r="11" fill="#fff"/><text x="32" y="30" text-anchor="middle" font-family="Open Sans,sans-serif" font-weight="600" font-size="16" fill="#2f6eae">1</text></svg>
    <p>Tax Disputes</p>
  </div>
  <div class="abs tile" style="left:703px">
    <svg width="56" height="60" viewBox="0 0 56 60"><circle cx="20" cy="6" r="5" fill="#fff"/><path d="M17 14v18h16l8 16 7-3" fill="none" stroke="#fff" stroke-width="5"/><path d="M12 26a16 16 0 1 0 20 22" fill="none" stroke="#fff" stroke-width="5"/></svg>
    <p>Medical Abuse</p>
  </div>
</section>

<main>
  <div class="abs band"></div>

  <h2 class="abs heading" style="left:92px;font-weight:400">WELCOME TO HALVENCOURT LAW GROUP, LLP</h2>
  <div class="abs team-photo" role="img" aria-label="Group of five smiling legal professionals standing together"></div>
  <p class="abs about-copy">Halvencourt Law Group, LLP provides quality legal representation to corporate as well as individual clients in the areas of business, corporate, securities, products liability, civil litigation (in State and Federal Courts), Alternative Dispute Resolution (arbitration and mediation), as well as a host of transactional matters.</p>
  <div class="abs more">MORE</div>

  <h2 class="abs heading" style="left:531px;font-weight:400">LATEST NEWS</h2>
  <div class="abs news-nav">
    <svg width="46" height="23" viewBox="0 0 46 23"><circle cx="11" cy="11.5" r="10" fill="none" stroke="#444" stroke-width="1.6"/><path d="M13 6l-5 5.5 5 5.5" fill="none" stroke="#444" stroke-width="1.8"/><circle cx="34" cy="11.5" r="10" fill="none" stroke="#444" stroke-width="1.6"/><path d="M32 6l5 5.5-5 5.5" fill="none" stroke="#444" stroke-width="1.8"/></svg>
  </div>

  <article class="abs news" style="top:777px">
    <div class="date"><div class="day">15</div><div class="month">MAR</div></div>
    <h3>DONEC RUTRUM PELLENTE</h3><h4>NAM MALESUADA NULLA MALSA</h4>
    <p>"I've had the opportunity to work with Meridian team members and can assure you they are professional, innovative and caring and they are always eager to help."</p>
  </article>
  <div class="abs news-rule" style="top:857px"></div>
  <article class="abs news" style="top:870px">
    <div class="date"><div class="day">15</div><div class="month">MAR</div></div>
    <h3>DONEC RUTRUM PELLENTE</h3><h4>NAM MALESUADA NULLA MALSA</h4>
    <p>"I've had the opportunity to work with Meridian team members and can assure you they are professional, innovative and caring and they are always eager to help."</p>
  </article>
  <div class="abs news-rule" style="top:955px"></div>
  <article class="abs news" style="top:971px">
    <div class="date"><div class="day">15</div><div class="month">MAR</div></div>
    <h3>DONEC RUTRUM PELLENTE</h3><h4>NAM MALESUADA NULLA MALSA</h4>
    <p>"I've had the opportunity to work with Meridian team members and can assure you they are professional, innovative and caring and they are always eager to help."</p>
  </article>
</main>

<footer>
  <div class="abs footer"></div>
  <div class="abs foot-links">Terms of Service | Returns | Policy Privacy | Event | Contact | Blog | Sitemap</div>
  <div class="abs copyright">Copy Right © 2014. All rights reserved.</div>
  <div class="abs social-foot"><span></span><span></span><span></span><span></span><span></span><span></span></div>
  <div class="abs newsletter">NEWS LETTER
    <svg width="28" height="16" viewBox="0 0 28 16"><rect x="1" y="1" width="26" height="14" fill="none" stroke="#222" stroke-width="2"/><path d="M1 1l13 9 13-9" fill="none" stroke="#222" stroke-width="2"/></svg>
  </div>
</footer>

</body>
</html>
```